Calvanta Group Real Estate Company business cards

New business card design, we are generally happy with the basic layout of the existing front of business card, (feel free to change) but require a head shot photo on the back side.

http://www.calvanta.com.au/

Attached logos, and existing business card

------------------------------

Target Market(s)

Real estate

Industry/Entity Type

Real Estate

Contact Information for Business Card

Standard size double sided

Font styles to use
Other font styles liked:
• Futura

Requirements
Must have
• Photo head shot on the back side
Nice to have
• yes
Should not have
• No

```html
<!DOCTYPE html>
<html lang="en">
<head>
<meta charset="utf-8">
<title>Calvanta Group – Business Cards</title>
<link href="https://fonts.googleapis.com/css2?family=Jost:wght@400;500&display=swap" rel="stylesheet">
<style>
  :root {
    --stage: #e6e4e1;
    --card: #161616;
    --card-edge: #222;
    --orange: #f7941d;
    --purple: #5b4bb7;
    --white: #f2f2f2;
    --rule: #8a8a8a;
    --photo-top: #2b3550;
    --photo-bottom: #1a1f2e;
  }
  * { margin: 0; padding: 0; box-sizing: border-box; }
  html, body { width: 1200px; height: 814px; overflow: hidden; }
  body {
    background: var(--stage);
    font-family: "Jost", sans-serif;
    position: relative;
  }
  .card {
    position: absolute;
    top: 242px;
    width: 540px;
    height: 330px;
    background: var(--card);
    border: 1px solid var(--card-edge);
    overflow: hidden;
  }
  .card--front { left: 40px; }
  .card--back { left: 620px; }

  /* Front */
  .front-brand {
    position: absolute;
    left: 40px;
    top: 150px;
    display: flex;
    align-items: center;
    gap: 12px;
    color: var(--orange);
    font-size: 30px;
    font-weight: 500;
  }
  .front-brand__square {
    width: 22px; height: 22px;
    background: var(--orange);
  }
  .front-divider {
    position: absolute;
    left: 262px;
    top: 82px;
    width: 1px;
    height: 160px;
    background: var(--rule);
  }
  .contact {
    position: absolute;
    left: 282px;
    top: 84px;
    color: var(--white);
    font-size: 14px;
    line-height: 19px;
  }
  .contact__name { color: var(--purple); font-size: 17px; font-weight: 500; }
  .contact__title { color: var(--orange); font-size: 14px; font-weight: 500; margin-bottom: 12px; }
  .contact__row { display: flex; align-items: center; gap: 8px; }
  .contact__row svg { width: 11px; height: 11px; flex: none; }
  .contact__spacer { height: 4px; }

  /* Back */
  .headshot {
    position: absolute;
    right: 0;
    top: 20px;
    width: 190px;
    height: 190px;
    background: linear-gradient(180deg, var(--photo-top), var(--photo-bottom));
  }
  .back-brand {
    position: absolute;
    left: 150px;
    top: 175px;
    color: var(--purple);
    font-size: 40px;
    font-weight: 400;
    letter-spacing: 0.5px;
  }
  .back-tagline {
    position: absolute;
    left: 200px;
    top: 228px;
    color: var(--purple);
    font-size: 11px;
    letter-spacing: 1px;
    word-spacing: 2px;
  }
  .back-url {
    position: absolute;
    left: 180px;
    top: 262px;
    color: var(--white);
    font-size: 14px;
    letter-spacing: 3px;
  }
</style>
</head>
<body>
  <section class="card card--front" aria-label="Business card front">
    <div class="front-brand">
      <span class="front-brand__square"></span>
      <span>Calvanta</span>
    </div>
    <div class="front-divider"></div>
    <div class="contact">
      <p class="contact__name">Daniel Tran</p>
      <p class="contact__title">Director</p>
      <p>Calvanta Group</p>
      <p>ABN: 12 345 678 901</p>
      <div class="contact__spacer"></div>
      <p class="contact__row">
        <svg viewBox="0 0 12 12" aria-hidden="true"><path fill="#5b4bb7" d="M2.5 1l2 2.5-1 1.2c.7 1.5 1.8 2.6 3.3 3.3l1.2-1L10.5 9 9.3 11C5 10.6 1.4 7 1 2.7z"/></svg>
        <span>0400 555 218</span>
      </p>
      <p class="contact__row">
        <svg viewBox="0 0 12 12" aria-hidden="true"><rect x="1" y="2.5" width="10" height="7" fill="#5b4bb7"/><path d="M1 2.5l5 4 5-4" stroke="#161616" fill="none"/></svg>
        <span>daniel.tran@calvanta.com.au</span>
      </p>
      <p class="contact__row">
        <svg viewBox="0 0 12 12" aria-hidden="true"><circle cx="6" cy="6" r="5" fill="#5b4bb7"/><path d="M1 6h10M6 1c-2.5 3-2.5 7 0 10M6 1c2.5 3 2.5 7 0 10" stroke="#161616" fill="none" stroke-width=".8"/></svg>
        <span>www.calvanta.com.au</span>
      </p>
    </div>
  </section>

  <section class="card card--back" aria-label="Business card back">
    <div class="headshot" role="img" aria-label="Head shot photo of the director in a navy suit"></div>
    <p class="back-brand">calvanta</p>
    <p class="back-tagline">Buy | Sell | Rent</p>
    <p class="back-url">www.calvanta.com.au</p>
  </section>
</body>
</html>
```